Business Card Design Project

business cards to match the logo design reference 1970674
specific details to be provided asap - message to follow
hello - thank you for the logo design (reference 1970674) which we are very happy with. In terms of business cards you presented a couple of options ie blue front/white back and then the reverse. Can we start with the white front version but change the text details to black font?
Actual details are as follows;
Dorian Plimsoll
Managing Director
e dorianplimsoll@kestrowe.com.au
t +61 2 5550 1937
m +61 400 555 219
Suite 712, Level 7, 48 Thornbury Rd
Sydney, NSW 2000, Australia
www.kestrowe.com.au

```html
<!DOCTYPE html>
<html lang="en">
<head>
<meta charset="utf-8">
<title>Kestrowe – Business Card</title>
<link rel="stylesheet" href="https://fonts.googleapis.com/css2?family=Jost:wght@400;500&display=swap">
<style>
  :root {
    --page-bg: #ffffff;
    --card-bg: #ffffff;
    --card-border: #e6e6e7;
    --brand-grey: #67686a;
    --brand-blue: #2a9fdc;
    --ink: #111111;
  }
  * { box-sizing: border-box; margin: 0; padding: 0; }
  html, body {
    width: 1200px;
    height: 1000px;
    overflow: hidden;
    background: var(--page-bg);
    font-family: "Jost", sans-serif;
    color: var(--ink);
  }
  .card {
    position: absolute;
    left: 73px;
    top: 199px;
    width: 1054px;
    height: 602px;
    background: var(--card-bg);
    border: 3px solid var(--card-border);
  }
  .brand {
    position: absolute;
    left: 212px;
    top: 90px;
    display: flex;
    align-items: center;
    gap: 44px;
  }
  .brand-mark {
    width: 128px;
    height: 128px;
    flex: none;
  }
  .brand-name {
    font-family: "Jost", sans-serif;
    font-weight: 500;
    font-size: 84px;
    line-height: 1;
    letter-spacing: 0.5px;
    color: var(--brand-grey);
  }
  .holder {
    position: absolute;
    left: 0;
    right: 0;
    top: 340px;
    text-align: center;
    white-space: nowrap;
  }
  .holder-name {
    font-size: 40px;
    font-weight: 400;
  }
  .holder-role {
    font-size: 24px;
    font-weight: 400;
    margin-left: 4px;
  }
  .contact {
    position: absolute;
    top: 451px;
    font-size: 24px;
    line-height: 41.5px;
    list-style: none;
    white-space: nowrap;
  }
  .contact-direct { left: 40px; }
  .contact-office { left: 582px; }
</style>
</head>
<body>
  <main class="card">
    <header class="brand">
      <svg class="brand-mark" viewBox="0 0 128 128" aria-hidden="true">
        <circle cx="64" cy="64" r="64" fill="var(--brand-blue)"/>
      </svg>
      <span class="brand-name">Kestrowe</span>
    </header>

    <p class="holder">
      <span class="holder-name">Dorian Plimsoll</span>
      <span class="holder-role">Managing Director</span>
    </p>

    <ul class="contact contact-direct">
      <li>e dorianplimsoll@kestrowe.com.au</li>
      <li>t +61 2 5550 1937</li>
      <li>m +61 400 555 219</li>
    </ul>

    <ul class="contact contact-office">
      <li>Suite 712, Level 7, 48 Thornbury Rd</li>
      <li>Sydney, NSW 2000, Australia</li>
      <li>www.kestrowe.com.au</li>
    </ul>
  </main>
</body>
</html>
```